Webdesign für Beratung von Firmen zum Thema Radon
Zielgruppe
Firmenname: Lumivelde - Ich informiere und berate als Radon Fachperson, Privatpersonen sowie Firmen zum Thema Radon, und die Gefahren die damit verbunden sind in bestehenden Gebäuden und Neubauten. Die Leistung erfolgt in Form eines ausgearbeiteten Sanierungskonzeptes bzw. bautechnische Maßnahmen beim Neubau.
Aufgabenstellung
Keep it simple and clean, weniger ist mehr. Die beigefügten Info-Grafiken sollen nur als Information dienen zum Thema Radon, und sollen nicht verwendet werden - ich hoffe hier doch besseres Bildmaterial von euch zu bekommen :-)

```html
<!DOCTYPE html>
<html lang="de">
<head>
<meta charset="utf-8">
<title>Lumivelde – Radon Beratung</title>
<link rel="stylesheet" href="https://fonts.googleapis.com/css2?family=Work+Sans:wght@400;500;600;700;800&display=swap">
<style>
:root{
  --ink:#1c1c1c;
  --muted:#6b6b6b;
  --blue:#1d5fa0;
  --green:#2e9a2e;
  --green-light:#3cc23c;
  --orange:#e38a12;
  --navy:#1f5b9c;
  --field:#b9b9b9;
  --white:#ffffff;
}
*{box-sizing:border-box;margin:0;padding:0}
html,body{width:1200px;height:3460px;overflow:hidden;background:var(--white)}
body{position:relative;font-family:"Work Sans",sans-serif;color:var(--ink)}
.site-header{position:absolute;left:0;top:0;width:1200px;height:109px;border-bottom:3px solid var(--green)}
.brand{position:absolute;display:flex;align-items:center;gap:8px;font-weight:700;font-size:15px;letter-spacing:1px;color:var(--green)}
.brand-dot{width:14px;height:14px;border-radius:50%;background:var(--green)}
.nav a{position:absolute;top:42px;font-size:19px;color:var(--muted);text-decoration:none;white-space:nowrap}
.section-title{position:absolute;font-weight:800;font-size:50px;letter-spacing:.5px;white-space:nowrap}
.band{position:absolute;left:0;width:1200px;height:11px}
.band-go{background:linear-gradient(var(--green) 0 50%,var(--orange) 50% 100%)}
.band-ob{background:linear-gradient(var(--orange) 0 50%,var(--navy) 50% 100%)}
.band-bg{background:linear-gradient(var(--navy) 0 50%,var(--green) 50% 100%)}
.card{position:absolute;background:var(--white);border-radius:28px;box-shadow:0 6px 16px rgba(0,0,0,.28)}
.photo{position:absolute;border-radius:26px}
.photo-portrait{background:radial-gradient(ellipse at 50% 40%,#efd6bd 0%,#d9b98f 35%,#b89466 65%,#8d7a68 100%)}
.photo-family{background:linear-gradient(180deg,#6fa6de 0%,#a9cdee 22%,#b24b3c 40%,#c9c9c4 60%,#e9e9e4 70%,#6f9e45 85%,#4f7f31 100%)}
.photo-villa{background:linear-gradient(180deg,#1f3f82 0%,#41609c 30%,#8c8a8a 48%,#e0a85a 62%,#6b5240 78%,#1e1e1e 100%)}
.expert-name{position:absolute;color:var(--blue);font-weight:600;font-size:23px;line-height:27px}
.expert-bio{position:absolute;color:var(--blue);font-size:15.5px;line-height:18.2px;width:152px}
.radon-info{position:absolute;left:692px;top:760px;width:414px}
.radon-info h3{font-size:18px;font-weight:600;line-height:21px}
.radon-info p{font-size:15.2px;line-height:18.2px;margin-bottom:22px;letter-spacing:.35px}
.cta{position:absolute;left:681px;top:1380px;width:351px;height:49px;border-radius:25px;background:linear-gradient(var(--green-light),var(--green));color:var(--white);font-weight:700;font-size:30px;text-align:center;line-height:49px;box-shadow:0 4px 10px rgba(0,0,0,.3)}
.lead{position:absolute;font-size:20px;font-weight:600;white-space:nowrap}
.step{position:absolute;left:88px;font-size:15px;white-space:nowrap}
.step h4{font-size:17px;font-weight:600;line-height:20px}
.project{position:absolute;font-size:15px;line-height:18px;white-space:nowrap}
.project h4{font-size:21px;font-weight:500;line-height:25px}
.project h5{font-size:18px;font-weight:600;line-height:22px}
.project.right{text-align:right}
.field{position:absolute;border:2px solid var(--field);font-size:20px;font-weight:600;color:#7a7a7a;padding:6px 6px}
.submit{position:absolute;left:87px;top:3312px;width:163px;height:39px;background:var(--green);color:var(--white);font-weight:700;font-size:21px;text-align:center;line-height:39px;border-radius:3px;box-shadow:0 3px 6px rgba(0,0,0,.3)}
.site-footer{position:absolute;left:0;top:3386px;width:1200px;height:74px;border-top:7px solid var(--green)}
.site-footer a{position:absolute;top:42px;font-size:19px;color:var(--muted);text-decoration:none}
</style>
</head>
<body>
<header class="site-header">
  <div class="brand" style="left:94px;top:42px"><span class="brand-dot"></span>LUMIVELDE</div>
  <nav class="nav">
    <a style="left:347px">Über uns</a>
    <a style="left:494px">Gefahren durch Radon</a>
    <a style="left:765px">Leistungen/Referenzen</a>
    <a style="left:1042px">Kontakt</a>
  </nav>
</header>

<h2 class="section-title" style="left:89px;top:122px">Unsere Experten</h2>
<div class="card" style="left:89px;top:195px;width:422px;height:416px"></div>
<div class="photo photo-portrait" role="img" aria-label="Porträtfoto einer lächelnden Expertin mit blonden Haaren" style="left:101px;top:206px;width:235px;height:395px"></div>
<div class="expert-name" style="left:348px;top:208px">Berta<br>Beispiel</div>
<div class="expert-bio" style="left:348px;top:262px">Lorem ipsum dolor sit amet, consetetur sadipscing elitr, sed diam nonuvmy eirmod tempor invidunt ut labore et dolore magna aliquyam erat, sed diam voluptua. At vero eos et accusam et justo duo dolores et ea rebum. Stet clita kasd gubergren, no sea takimata sanctus est.</div>
<div class="card" style="left:692px;top:195px;width:422px;height:416px"></div>
<div class="photo photo-portrait" role="img" aria-label="Porträtfoto einer lächelnden Expertin mit blonden Haaren" style="left:704px;top:206px;width:235px;height:395px"></div>
<div class="expert-name" style="left:951px;top:208px">Berta<br>Beispiel</div>
<div class="expert-bio" style="left:951px;top:262px">Lorem ipsum dolor sit amet, consetetur sadipscing elitr, sed diam nonuvmy eirmod tempor invidunt ut labore et dolore magna aliquyam erat, sed diam voluptua. At vero eos et accusam et justo duo dolores et ea rebum. Stet clita kasd gubergren, no sea takimata sanctus est.</div>

<div class="band band-go" style="top:637px"></div>

<h2 class="section-title" style="left:94px;top:675px">Gefahren durch Radon</h2>
<div class="card" role="img" aria-label="3D-Illustration eines Hauses im Schnitt, in das Radon aus dem Boden eindringt" style="left:87px;top:759px;width:421px;height:361px;background:linear-gradient(170deg,#f7f8f9 0%,#dfe3e6 45%,#c9ced3 62%,#eceef0 80%,#e2e5e8 100%)"></div>
<div class="card" role="img" aria-label="Periodensystem mit metallischer Kugel für das Element Radon" style="left:87px;top:1173px;width:421px;height:265px;background:radial-gradient(circle at 76% 48%,#b3aea6 0%,#6e6a64 14%,#4a4a4a 30%,#3a3a3a 60%,#262626 100%)"></div>
<div class="radon-info">
  <h3>Was ist Radon?</h3>
  <p>Radon ist ein radioaktives Gas, welches im Boden entsteht. Für den Menschen ist es gefährlich, denn es ist krebserregend: Radon ist laut der Hallbrook University die zweithäufigste Ursache für Lungenkrebs.</p>
  <h3>Was passiert mit dem Radon?</h3>
  <p>Das Radon gelangt durch durchlässige Böden und Fundamente in Kellerräume und letztendlich auch in Wohnräume. Die Radonkonzentration steigt. Radon-Moleküle setzen sich an Partikel wie Staub oder Tabakrauch fest. Zusammen mit diesen Partikel gelangt Radon in die Lunge und richtet dort Schaden an. (Passiv-)Raucher-Haushalte sind also besonders gefährdet.</p>
  <h3>Ist jede Region gleich stark betroffen?</h3>
  <p>Nein. Die Belastung ist sogar lokal unterschiedlich, weshalb die tatsächliche Belastung nur durch professionelle Messungen festgestellt werden kann.</p>
  <h3>Wie kann ich mich schützen?</h3>
  <p>Wir beraten Sie individuell, um für Sie eine ideale und individuelle Lösung finden zu können. Wir greifen hier auf unser Fachwissen und unsere Erfahrung zurück.</p>
  <h3>Sind Neubauten betroffen?</h3>
  <p>Ja, auch Neubauten sind ohne entsprechenden Schutz gefährdet. Auch in diesem Bereich beraten wir Sie gerne.</p>
</div>
<div class="cta">Jetzt anfragen</div>

<div class="band band-ob" style="top:1469px"></div>

<h2 class="section-title" style="left:88px;top:1508px">Leistungen/Referenzen</h2>
<div class="lead" style="left:88px;top:1593px">So schützen wir ihre Gesundheit:</div>
<div class="step" style="top:1637px"><h4>Erste Stufe</h4><b>Wir begutachten Ihr Objekt</b> und <b>beraten Sie umfassend</b>. Hierbei profitieren Sie von unserer <b>Expertise</b>.</div>
<div class="step" style="top:1695px"><h4>Zweite Stufe</h4><b>Wir sanieren ihr Objekt</b>. So ist sichergestellt, dass Sie in Zukunft <b>ohne gesundheitsschädliche Radon-Belastung leben</b> können.</div>
<div class="lead" style="left:88px;top:1772px">Wir haben Ihnen folgend einige unserer Referenzen aufgelistet:</div>

<div class="card" style="left:87px;top:1822px;width:593px;height:237px"></div>
<div class="photo photo-family" role="img" aria-label="Foto einer Familie, die vor ihrem roten Holzhaus über die Wiese läuft" style="left:99px;top:1848px;width:237px;height:186px"></div>
<div class="project" style="left:347px;top:1850px"><h4>Projekt 1</h4><h5>Projektbeschreibung</h5>- Besonderheit 1<br>- Besonderheit 2<br>- Besonderheit 3</div>

<div class="card" style="left:519px;top:2160px;width:594px;height:238px"></div>
<div class="photo photo-villa" role="img" aria-label="Foto eines modernen, beleuchteten Hauses in der Abenddämmerung" style="left:864px;top:2187px;width:235px;height:184px"></div>
<div class="project right" style="right:345px;top:2188px"><h4>Projekt 2</h4><h5>Projektbeschreibung</h5>- Besonderheit 1<br>- Besonderheit 2<br>- Besonderheit 3</div>

<div class="card" style="left:87px;top:2485px;width:593px;height:238px"></div>
<div class="photo photo-family" role="img" aria-label="Foto einer Familie, die vor ihrem roten Holzhaus über die Wiese läuft" style="left:99px;top:2511px;width:237px;height:186px"></div>
<div class="project" style="left:347px;top:2513px"><h4>Projekt 1</h4><h5>Projektbeschreibung</h5>- Besonderheit 1<br>- Besonderheit 2<br>- Besonderheit 3</div>

<div class="band band-bg" style="top:2752px"></div>

<h2 class="section-title" style="left:88px;top:2778px">Kontaktieren Sie uns</h2>
<div class="lead" style="left:88px;top:2862px">Wir erstellen Ihnen gerne ein individuelles Angebot</div>
<div class="field" style="left:87px;top:2912px;width:335px;height:39px">Vorname</div>
<div class="field" style="left:433px;top:2912px;width:334px;height:39px">Nachname</div>
<div class="field" style="left:87px;top:2977px;width:335px;height:39px">E-Mail-Adresse</div>
<div class="field" style="left:87px;top:3043px;width:593px;height:242px">Ihre Anfrage</div>
<div class="submit">Abschicken</div>

<footer class="site-footer">
  <div class="brand" style="left:92px;top:30px;font-size:13px"><span class="brand-dot" style="width:12px;height:12px"></span>LUMIVELDE</div>
  <a style="left:751px">Impressum</a>
  <a style="left:997px">Datenschutz</a>
</footer>
</body>
</html>
```